Business Card Design

We have our logo and everything in place. Looking to have a layout for our new business cards designed. These will be printed with a matte finish, possibly rounded corners, and looking to incorporate some cool spot UV layers into the design.

Ive uploaded the existing card front and back as well as our logo.

Card Size Will Be 3.5" x 2"

```html
<!DOCTYPE html>
<html lang="en">
<head>
<meta charset="utf-8">
<title>Ridgeline Deck &amp; Rail — Business Cards</title>
<link rel="stylesheet" href="https://fonts.googleapis.com/css2?family=Open+Sans:wght@400;600&display=swap">
<style>
  :root {
    --backdrop: #8f8f8f;
    --card: #e9e9ec;
    --ink: #111111;
    --ink-soft: #222222;
  }
  * { box-sizing: border-box; margin: 0; padding: 0; }
  html, body {
    width: 1105px;
    height: 1200px;
    overflow: hidden;
  }
  body {
    position: relative;
    background: var(--backdrop);
    font-family: "Open Sans", Arial, sans-serif;
    color: var(--ink);
  }
  .card {
    position: absolute;
    left: 182px;
    width: 746px;
    height: 424px;
    background: var(--card);
    border-radius: 22px;
  }
  .card--front { top: 119px; }
  .card--back  { top: 637px; }

  .brand-name {
    position: absolute;
    font-weight: 600;
    color: var(--ink);
    text-align: center;
    line-height: 1.15;
  }
  .card--front .brand-name {
    left: 56px;
    top: 150px;
    width: 292px;
    font-size: 34px;
  }
  .card--back .brand-name {
    left: 0;
    right: 0;
    top: 160px;
    font-size: 46px;
  }

  .contact-block {
    position: absolute;
    left: 370px;
    top: 120px;
  }
  .person-name {
    font-size: 25px;
    font-weight: 600;
    line-height: 1.2;
  }
  .person-title {
    font-size: 19px;
    font-weight: 400;
    color: var(--ink-soft);
    margin-top: 2px;
  }
  .contact-list {
    list-style: none;
    margin-top: 24px;
  }
  .contact-item {
    display: flex;
    align-items: center;
    gap: 10px;
    font-size: 18px;
    line-height: 28px;
    color: var(--ink-soft);
  }
  .contact-icon {
    width: 15px;
    height: 15px;
    flex: none;
    fill: var(--ink);
  }
</style>
</head>
<body>

  <section class="card card--front" aria-label="Card front">
    <div class="brand-name">Ridgeline<br>Deck &amp; Rail</div>

    <div class="contact-block">
      <p class="person-name">Marcus Ellery</p>
      <p class="person-title">President</p>
      <ul class="contact-list">
        <li class="contact-item">
          <svg class="contact-icon" viewBox="0 0 16 16" aria-hidden="true">
            <path d="M3.6 1.2l2.3 2.6c.4.4.4 1 0 1.4L4.7 6.5c.9 2 2.6 3.7 4.8 4.8l1.3-1.2c.4-.4 1-.4 1.4 0l2.6 2.3c.4.4.4 1 0 1.4l-1.4 1.4C10.6 16.2 0 5.6 1.8 2.8L3.2 1.2c.1-.1.3-.1.4 0z"/>
          </svg>
          403.555.0187
        </li>
        <li class="contact-item">
          <svg class="contact-icon" viewBox="0 0 16 16" aria-hidden="true">
            <path d="M1 3h14v1.2L8 8.8 1 4.2z"/>
            <path d="M1 5.6l7 4.6 7-4.6V13H1z"/>
          </svg>
          hello@ridgelinedeckrail.com
        </li>
        <li class="contact-item">
          <svg class="contact-icon" viewBox="0 0 16 16" aria-hidden="true">
            <circle cx="8" cy="8" r="7"/>
            <path d="M1 8h14M8 1c2.4 2.2 2.4 11.8 0 14M8 1c-2.4 2.2-2.4 11.8 0 14" stroke="#e9e9ec" stroke-width="1.1" fill="none"/>
          </svg>
          www.ridgelinedeckrail.com
        </li>
      </ul>
    </div>
  </section>

  <section class="card card--back" aria-label="Card back">
    <div class="brand-name">Ridgeline<br>Deck &amp; Rail</div>
  </section>

</body>
</html>
```